Coastal Heritage Dairywrights' Guild needs new business cards

We need new business cards designed and produced. We are likely to need other design work done for ads, flyers etc in future.

We would like to start with an initial business card.

The Coastal Heritage Dairywrights' Guild (CHDG) is a membership-based not-for-profit organisation that looks after the interests of Australia's small to medium artisan cheesemakers, many of whom are also small-scale farmers. The design should be simple, using our logo, but also communicate our artisan cheese and small dairy farm focus.

The first card to be designed and produced is for me, Megan Thorburn. My details are:

Megan Thorburn
Secretary
Coastal Heritage Dairywrights' Guild (CHDG)
http://www.curdandcrockery.org
T +61427583914
E megan.meganthorburn@mailfern.net

I have attached the CHDG logo in jpg form. I have a higher resolution version available if needed.

Thank you!

Megan

Business

Megan Thorburn
Coastal Heritage Dairywrights' Guild
megan.meganthorburn@mailfern.net
+61427583914

Sans Serif

• Logo (see attached file)

```html
<!DOCTYPE html>
<html lang="en">
<head>
<meta charset="utf-8">
<title>Coastal Heritage Dairywrights' Guild — Business Card</title>
<link rel="stylesheet" href="https://fonts.googleapis.com/css2?family=Cabin:wght@400&family=Roboto+Condensed:wght@700&display=swap">
<style>
  :root {
    --backdrop: #c9c9c9;
    --card: #ffffff;
    --brown: #5b3a1f;
    --cheese: #fbcf6e;
    --cheese-rind: #6a421f;
  }
  * { margin: 0; padding: 0; box-sizing: border-box; }
  html, body {
    width: 1200px;
    height: 1000px;
    overflow: hidden;
    background: var(--backdrop);
  }
  .canvas {
    position: relative;
    width: 1200px;
    height: 1000px;
  }
  .card {
    position: absolute;
    left: 160px;
    top: 240px;
    width: 880px;
    height: 520px;
    background: var(--card);
    border-radius: 28px;
    overflow: hidden;
    font-family: "Cabin", "Gill Sans", sans-serif;
    color: var(--brown);
  }
  .org-mark {
    position: absolute;
    left: 100px;
    top: 56px;
    display: flex;
    align-items: flex-start;
    gap: 18px;
  }
  .org-mark__dot {
    width: 58px;
    height: 58px;
    border-radius: 50%;
    background: var(--cheese);
    flex: none;
    margin-top: 4px;
  }
  .org-mark__name {
    font-size: 26px;
    line-height: 1.12;
    color: var(--brown);
  }
  .contact {
    position: absolute;
    left: 40px;
    top: 330px;
    list-style: none;
  }
  .contact__item {
    display: flex;
    align-items: center;
    gap: 14px;
    font-size: 21px;
    height: 40px;
    white-space: nowrap;
  }
  .contact__icon {
    width: 26px;
    height: 26px;
    flex: none;
  }
  .cheese {
    position: absolute;
    left: 460px;
    top: 70px;
    width: 500px;
    height: 500px;
    border-radius: 50%;
    background: var(--cheese);
    box-shadow: 0 0 0 8px var(--card), 0 0 0 16px var(--cheese-rind);
  }
  .person {
    position: absolute;
    left: 490px;
    top: 250px;
    width: 320px;
    text-align: right;
  }
  .person__name {
    font-family: "Roboto Condensed", "Arial Narrow", sans-serif;
    font-weight: 700;
    font-size: 38px;
    letter-spacing: 0.5px;
    text-transform: uppercase;
    color: var(--brown);
    white-space: nowrap;
  }
  .person__role {
    font-size: 25px;
    margin-top: 2px;
    color: var(--brown);
  }
</style>
</head>
<body>
<div class="canvas">
  <div class="card">
    <div class="cheese" role="img" aria-label="Illustration of a round wheel of cheese with holes and a hand-drawn rind"></div>

    <div class="org-mark">
      <span class="org-mark__dot"></span>
      <div class="org-mark__name">Coastal<br>Heritage<br>Dairywrights'<br>Guild</div>
    </div>

    <ul class="contact">
      <li class="contact__item">
        <svg class="contact__icon" viewBox="0 0 26 26" aria-hidden="true">
          <circle cx="13" cy="13" r="13" fill="var(--cheese)"/>
          <path d="M9 7.5c1 0 1.5.5 2 2l-1.2 1.4c.7 1.7 1.9 3 3.6 3.6L15 13.3c1.5.5 2 1 2 2 0 1.3-1 2.2-2.2 2.2-4.3-.3-7.6-3.6-8-8C6.8 8.4 7.7 7.5 9 7.5z" fill="var(--brown)"/>
        </svg>
        <span>+61 (427) 583 914</span>
      </li>
      <li class="contact__item">
        <svg class="contact__icon" viewBox="0 0 26 26" aria-hidden="true">
          <circle cx="13" cy="13" r="13" fill="var(--cheese)"/>
          <rect x="6.5" y="8.5" width="13" height="9" fill="none" stroke="var(--brown)" stroke-width="1.5"/>
          <path d="M6.5 8.5 13 14l6.5-5.5" fill="none" stroke="var(--brown)" stroke-width="1.5"/>
        </svg>
        <span>megan.meganthorburn@mailfern.net</span>
      </li>
      <li class="contact__item">
        <svg class="contact__icon" viewBox="0 0 26 26" aria-hidden="true">
          <circle cx="13" cy="13" r="13" fill="var(--cheese)"/>
          <circle cx="13" cy="13" r="6.5" fill="none" stroke="var(--brown)" stroke-width="1.4"/>
          <ellipse cx="13" cy="13" rx="2.8" ry="6.5" fill="none" stroke="var(--brown)" stroke-width="1.2"/>
          <path d="M6.5 13h13" stroke="var(--brown)" stroke-width="1.2"/>
        </svg>
        <span>www.curdandcrockery.org</span>
      </li>
    </ul>

    <div class="person">
      <div class="person__name">Megan Thorburn</div>
      <div class="person__role">Secretary</div>
    </div>
  </div>
</div>
</body>
</html>
```